Re-design my Shearing Contract Estimate format.

The one page contract estimate is the output of a Farmer going online to our website and creating their shearing contract estimate.
The design should follow our current branding.
I have uploaded the current contract estimate design and a screen shot of our home page

```html
<!DOCTYPE html>
<html lang="en">
<head>
<meta charset="UTF-8">
<title>Shearing Contract Estimate</title>
<link rel="stylesheet" href="https://fonts.googleapis.com/css2?family=Poppins:wght@400;500;600&display=swap">
<style>
  :root {
    --canvas: #ececec;
    --page: #ffffff;
    --forest: #224a36;
    --label-bg: #eff7f2;
    --value-bg: #cbe9d3;
    --ring: #cdebd5;
    --ink: #224a36;
  }
  * { box-sizing: border-box; margin: 0; padding: 0; }
  html, body {
    width: 1200px; height: 1200px; overflow: hidden;
    background: var(--canvas);
    font-family: "Poppins", sans-serif;
    color: var(--ink);
  }
  .estimate-page {
    position: absolute; left: 147px; top: 0;
    width: 905px; height: 1200px;
    background: var(--page);
  }
  .brand-band {
    position: absolute; left: 0; top: 0;
    width: 100%; height: 163px;
    background: var(--forest);
  }
  .brand-badge {
    position: absolute; left: 339px; top: 33px;
    width: 226px; height: 226px; border-radius: 50%;
    background: var(--page);
    border: 12px solid var(--ring);
    display: flex; align-items: center; justify-content: center;
  }
  .brand-name {
    font-weight: 600; font-size: 42px; letter-spacing: 1px;
    color: var(--forest);
  }
  .estimate-block {
    position: absolute; left: 57px; width: 790px;
  }
  .section-heading {
    height: 27px; border-radius: 14px;
    background: var(--forest); color: #fff;
    font-size: 14px; font-weight: 500;
    display: flex; align-items: center; justify-content: center;
    margin-bottom: 2px;
  }
  .field-row {
    display: flex; gap: 3px; height: 25.5px; margin-bottom: 3.2px;
    font-size: 14px;
  }
  .field-label {
    flex: 0 0 473px; background: var(--label-bg);
    border-radius: 13px 0 0 13px;
    padding-left: 20px; display: flex; align-items: center;
    font-weight: 400;
  }
  .field-label.strong { font-weight: 500; }
  .field-value {
    flex: 1; background: var(--value-bg);
    border-radius: 0 13px 13px 0;
    padding-right: 22px; display: flex; align-items: center; justify-content: flex-end;
    font-weight: 600;
  }
</style>
</head>
<body>
  <main class="estimate-page">
    <div class="brand-band"></div>
    <div class="brand-badge"><span class="brand-name">KELSO</span></div>

    <section class="estimate-block" style="top:299px">
      <div class="field-row"><div class="field-label strong">Contract No.</div><div class="field-value">2</div></div>
      <div class="field-row"><div class="field-label strong">Grower Details</div><div class="field-value"></div></div>
    </section>

    <section class="estimate-block" style="top:393px">
      <h2 class="section-heading">Sheep / Shearing Type</h2>
      <div class="field-row"><div class="field-label strong">Merinos</div><div class="field-value">20,000</div></div>
      <div class="field-row"><div class="field-label strong">XB Ewes</div><div class="field-value">10,000</div></div>
      <div class="field-row"><div class="field-label strong">Lambs</div><div class="field-value"></div></div>
      <div class="field-row"><div class="field-label strong">Full Crutch</div><div class="field-value"></div></div>
      <div class="field-row"><div class="field-label strong">Mkt Crutch</div><div class="field-value"></div></div>
      <div class="field-row"><div class="field-label strong">Rams</div><div class="field-value"></div></div>
      <div class="field-row"><div class="field-label strong">Total Number of Sheep</div><div class="field-value">30,000</div></div>
      <div class="field-row"><div class="field-label strong">Number of Shed Stands</div><div class="field-value">8</div></div>
    </section>

    <section class="estimate-block" style="top:695px">
      <h2 class="section-heading">Wool Staff Requirements</h2>
      <div class="field-row"><div class="field-label">Wool Handler</div><div class="field-value">3</div></div>
      <div class="field-row"><div class="field-label">Wool Classer</div><div class="field-value">1</div></div>
      <div class="field-row"><div class="field-label">Wool Presser / Penner (Combined Role)</div><div class="field-value"></div></div>
      <div class="field-row"><div class="field-label">Wool Presser</div><div class="field-value">0</div></div>
      <div class="field-row"><div class="field-label">Penner</div><div class="field-value">1</div></div>
    </section>

    <section class="estimate-block" style="top:909px">
      <h2 class="section-heading">Estimated Contract Price</h2>
      <div class="field-row"><div class="field-label">Total Shearing Contract Cost</div><div class="field-value">$178,458.00</div></div>
      <div class="field-row"><div class="field-label">Total Wool Staff Contract Cost</div><div class="field-value">$38,745.00</div></div>
      <div class="field-row"><div class="field-label strong">Total Exl GST</div><div class="field-value">$217,203.00</div></div>
      <div class="field-row"><div class="field-label strong">Total Inc GST</div><div class="field-value">$238,923.00</div></div>
      <div class="field-row"><div class="field-label">Total Estimated per Sheep</div><div class="field-value">$7.96</div></div>
    </section>
  </main>
</body>
</html>
```